Vellum Systemics Buisness Cards

I need a technology focused clean business card for my employees. I have attached out logo to include in the mocks. We're a modern tech consulting firm that drives to interface humanity with technology in a truly cohesive fashion.

```html
<!DOCTYPE html>
<html lang="en">
<head>
<meta charset="utf-8">
<title>Vellum Systemics – Business Card</title>
<link rel="stylesheet" href="https://fonts.googleapis.com/css2?family=Arimo:wght@400;700&display=swap">
<style>
  :root {
    --card-bg: #030607;
    --ink-white: #ffffff;
    --brand-blue: #1a74bb;
    --brand-grey: #8d8f91;
    --divider: #d4d4d4;
  }
  html, body {
    margin: 0;
    padding: 0;
    width: 1200px;
    height: 685px;
    overflow: hidden;
    background: var(--card-bg);
  }
  .card {
    position: relative;
    width: 1200px;
    height: 685px;
    background: var(--card-bg);
    font-family: "Arimo", Arial, sans-serif;
    color: var(--ink-white);
    overflow: hidden;
  }
  .brand {
    position: absolute;
    left: 143px;
    top: 309px;
    height: 60px;
    display: flex;
    align-items: center;
    gap: 14px;
  }
  .brand-dot {
    width: 34px;
    height: 34px;
    border-radius: 50%;
    background: var(--brand-blue);
    flex: none;
  }
  .brand-name {
    font-weight: 700;
    font-size: 36px;
    line-height: 1;
    color: var(--brand-grey);
    white-space: nowrap;
  }
  .divider {
    position: absolute;
    left: 598px;
    top: 168px;
    width: 2px;
    height: 355px;
    background: var(--divider);
  }
  .line {
    position: absolute;
    left: 639px;
    margin: 0;
    line-height: 1;
    white-space: nowrap;
  }
  .person-name {
    left: 643px;
    top: 164px;
    font-size: 48px;
    font-weight: 700;
  }
  .person-name .surname { color: var(--brand-blue); }
  .person-role {
    left: 643px;
    top: 216px;
    font-size: 31px;
  }
  .contact { font-size: 31px; }
  .contact-phone { top: 295px; }
  .contact-email { top: 353px; }
  .contact-web { top: 390px; }
  .contact-street { top: 449px; }
  .contact-city { top: 488px; }
</style>
</head>
<body>
  <main class="card">
    <div class="brand">
      <span class="brand-dot"></span>
      <span class="brand-name">Vellum Systemics</span>
    </div>

    <div class="divider"></div>

    <h1 class="line person-name">Marcus <span class="surname">Ellery</span></h1>
    <p class="line person-role">Manager</p>

    <p class="line contact contact-phone">012-555-0147</p>
    <p class="line contact contact-email">info@vellumsystemics.com</p>
    <p class="line contact contact-web">www.vellumsystemics.com</p>
    <p class="line contact contact-street">1480 Larkspur Avenue</p>
    <p class="line contact contact-city">Juneau, AK 99801</p>
  </main>
</body>
</html>
```